Tovendi: National Baking Mix Company Needs a Pancake And Waffle Mix Label Design

Hi, we are looking for a front label design for a new pancake and waffle mix. We currently develop and manufacture various dry mixes for crepes, pancakes, waffles, and waffle cones. We are looking to expand our product line into the "all natural" category of foods. This new pancake mix contains the highest quality ingredients including: (whole grain brown rice flour, whole grain oat flour, golden flaxseed meal, whole grain sorghum flour, organic coconut flour, organic coconut sugar, eggs, leavening, vanilla extract, salt, spices.) We are looking for a way to communicate these ingredients to the public by means of claims like one would see on a food label. Here are a few different companies that do it well.
https://oakmillers.example/product/harvest/
https://www.quietgrove.example/collections/almond-flour-baking-mixes/products/almond-flour-pancake-waffle-mix
https://fentonoven.example/product/harvest-pancake-waffle-mix/
https://tovendi.example
Our mix is a just add water only mix and consists of whole grains, is gluten free, dairy free, soy free, preservative free, contains no artificial ingredients whatsoever, NON-GMO, kosher, low in sodium, good source of fiber and iron, contains omega-3 fatty acids etc. We need a strong and attractive design that appeals to the customer on a grocery store shelf. This mix is a healthier option compared to traditional pancake/waffle mixes but still provides great taste and texture one would expect from a pancake mix. Label design should be around 4.25"x 6.75" tall ways. We want to utilize what we have to offer in the best way possible.

Target Market(s)

All Natural, Healthy, Pancake Mix. 20yr-50yr olds primariliy

Industry/Entity Type

Grocery Store

Font styles to use
Serif
Sans Serif
Decorative

Colors

Designer to choose colors to be used in the design.

Requirements
Must have
• Name of company "Tovendi", must say "Pancake & Waffle Mix", "Just add water", "gluten free", "dairy free", "whole grains". the rest is up to you!
Nice to have
• I would like to see the claims utilized and promoted in such ways that appeal to the consumer. The all natural category of food is growing and we want to take advantage of that food category.
Should not have
• Should not say "paleo" on label. This mix is within the category but cannot be labeled as such.

```html
<!DOCTYPE html>
<html lang="en">
<head>
<meta charset="utf-8">
<title>Tovendi Pancake &amp; Waffle Mix Label</title>
<link rel="stylesheet" href="https://fonts.googleapis.com/css2?family=Amatic+SC:wght@700&family=Titan+One&display=swap">
<style>
  :root {
    --page: #ffffff;
    --chocolate: #562f14;
    --kraft: #8c6b4f;
    --kraft-light: #977758;
    --berry: #921b20;
    --cream: #f4e7d2;
    --ink: #141008;
    --white: #ffffff;
  }
  html, body {
    margin: 0;
    width: 1200px;
    height: 1200px;
    overflow: hidden;
    background: var(--page);
  }
  .label {
    position: absolute;
    left: 236px;
    top: 22px;
    width: 728px;
    height: 1156px;
    background: var(--white);
    font-family: "Amatic SC", cursive;
  }
  .top-band {
    position: absolute;
    left: 0; top: 0;
    width: 728px; height: 80px;
    background: var(--chocolate);
  }
  .brand-name {
    position: absolute;
    left: 0; top: 62px;
    width: 728px;
    text-align: center;
    font-family: "Titan One", sans-serif;
    font-size: 46px;
    line-height: 1;
    color: var(--cream);
    z-index: 3;
  }
  .brand-name span {
    display: inline-block;
    background: var(--chocolate);
    padding: 10px 34px 14px;
    border-radius: 8px;
  }
  .hero-photo {
    position: absolute;
    left: 0; top: 86px;
    width: 728px; height: 508px;
    background: radial-gradient(ellipse at 55% 45%, #e6c48e 0%, #c99a63 30%, #a87650 60%, #7f5638 100%);
  }
  .kraft-panel {
    position: absolute;
    left: 0; top: 600px;
    width: 728px; height: 556px;
    background: linear-gradient(180deg, var(--kraft-light), var(--kraft));
  }
  .title-banner {
    position: absolute;
    left: 62px; top: 494px;
    width: 604px; height: 228px;
    box-sizing: border-box;
    background: var(--berry);
    border: 6px solid var(--white);
    text-align: center;
    color: var(--white);
  }
  .title-banner h1 {
    margin: 24px 0 0;
    font-family: "Titan One", sans-serif;
    font-weight: 400;
    font-size: 80px;
    line-height: 74px;
    letter-spacing: 2px;
    white-space: nowrap;
  }
  .title-banner .promise {
    margin: 14px 0 0;
    font-size: 22px;
    line-height: 26px;
    letter-spacing: 0.5px;
    white-space: nowrap;
  }
  .ribbon {
    position: absolute;
    left: 200px; top: 440px;
    width: 330px; height: 90px;
    z-index: 2;
  }
  .ribbon-text {
    position: absolute;
    left: 240px; top: 446px;
    width: 248px;
    text-align: center;
    font-size: 46px;
    line-height: 60px;
    color: var(--berry);
    z-index: 3;
  }
  .claims-main {
    position: absolute;
    right: 428px; top: 770px;
    text-align: right;
    font-size: 70px;
    line-height: 68px;
    color: var(--ink);
  }
  .claims-stars {
    position: absolute;
    left: 311px; top: 780px;
    width: 22px;
    height: 200px;
  }
  .claims-detail {
    position: absolute;
    left: 342px; top: 780px;
    font-size: 38px;
    line-height: 50px;
    color: var(--ink);
    white-space: nowrap;
  }
  .claims-main p, .claims-detail p { margin: 0; }
  .ingredients {
    position: absolute;
    left: 62px; top: 1018px;
    width: 604px; height: 138px;
    background: var(--chocolate);
    color: var(--cream);
    font-size: 24px;
    line-height: 31px;
    text-align: center;
    box-sizing: border-box;
    padding: 20px 24px 0;
  }
  .ingredients strong { font-weight: 700; }
</style>
</head>
<body>
<div class="label">
  <div class="top-band"></div>
  <div class="hero-photo" role="img" aria-label="Stack of golden pancakes with maple syrup on a white plate, on a rustic wooden table with a glass bowl of honey and a red gingham cloth"></div>
  <div class="brand-name"><span>Tovendi</span></div>
  <div class="kraft-panel"></div>

  <div class="title-banner">
    <h1>PANCAKE &amp;<br>WAFFLE MIX</h1>
    <p class="promise">CONTAINS NO ARTIFICIAL INGREDIENTS WHATSOEVER!</p>
  </div>

  <svg class="ribbon" viewBox="0 0 330 90" aria-hidden="true">
    <polygon points="0,22 44,22 44,70 0,70 14,46" fill="#921b20" stroke="#ffffff" stroke-width="4"/>
    <polygon points="330,22 286,22 286,70 330,70 316,46" fill="#921b20" stroke="#ffffff" stroke-width="4"/>
    <rect x="38" y="6" width="254" height="72" fill="#ffffff"/>
    <rect x="44" y="12" width="242" height="60" fill="none" stroke="#921b20" stroke-width="2"/>
  </svg>
  <div class="ribbon-text">JUST ADD WATER</div>

  <div class="claims-main">
    <p>Gluten Free</p>
    <p>Dairy Free</p>
    <p>Whole Grains</p>
  </div>

  <svg class="claims-stars" viewBox="0 0 22 200" aria-hidden="true" fill="#141008">
    <g id="star"><polygon points="11,2 13.5,8.5 20,8.5 14.8,12.6 16.8,19 11,15 5.2,19 7.2,12.6 2,8.5 8.5,8.5"/></g>
    <use href="#star" y="42"/>
    <use href="#star" y="84"/>
    <use href="#star" y="126"/>
    <use href="#star" y="168"/>
  </svg>

  <div class="claims-detail">
    <p>Soy Free • Kosher • Low In Sodium</p>
    <p>Good Source Of Fiber And Iron</p>
    <p>Preservative Free • Non GMO</p>
    <p>Contains Omega-3 Fatty Acids</p>
  </div>

  <div class="ingredients">
    <strong>Ingredients:</strong> Whole Grain Brown Rice Flour, Whole Grain Oat Flour, Golden Flaxseed Meal, Whole Grain Sorghum Flour, Organic Coconut Flour, Organic Coconut Sugar, Eggs, Leavening, Vanilla Extract, Salt, Spices.
  </div>
</div>
</body>
</html>
```